Fermoso Habitar Presentation

We already have a logo, and now we need a good presentation for our company. You can seach for us at : fermosohabitar.pt and see more about us. We work in adaptive reuse of buildings. You can ask anything you need to do a great job.

Industry/Entity Type

It Company

```html
<!DOCTYPE html>
<html lang="en">
<head>
<meta charset="utf-8">
<title>Fermoso Habitar – Presentation Template</title>
<link rel="stylesheet" href="https://fonts.googleapis.com/css2?family=Arimo:wght@400;700&family=Carlito:wght@400;700&display=swap">
<style>
  :root {
    --stage: #e9e6e1;
    --slide: #ffffff;
    --brand: #3b6ec2;
    --ink: #111111;
    --rule: #1a1a1a;
    --band: #0b0b0b;
    --photo-grey: #bdbdbd;
    --photo-blue: #4b83d0;
    --series-1: #3d6fc9;
    --series-2: #d23a36;
    --series-3: #8fc23c;
    --grid: #c9c9c9;
    --page-dot: #3f78c8;
  }
  * { box-sizing: border-box; margin: 0; padding: 0; }
  html, body { width: 1200px; height: 884px; overflow: hidden; background: var(--stage); }
  body { position: relative; font-family: "Arimo", Arial, sans-serif; color: var(--ink); }

  .slide {
    position: absolute; width: 544px; height: 405px;
    background: var(--slide); overflow: hidden;
  }
  .slide--cover  { left: 35px;  top: 23px; }
  .slide--points { left: 630px; top: 23px; }
  .slide--chart  { left: 35px;  top: 444px; }
  .slide--thanks { left: 630px; top: 444px; }

  .abs { position: absolute; }

  /* brand name block */
  .brand { position: absolute; text-align: center; color: var(--brand); font-weight: 700; letter-spacing: -0.3px; }
  .brand__dot { display: block; margin: 0 auto; border-radius: 50%; background: var(--brand); }
  .brand--cover { left: 0; right: 0; top: 16px; font-size: 23px; }
  .brand--cover .brand__dot { width: 26px; height: 26px; margin-bottom: 3px; }
  .brand--small { width: 150px; font-size: 13px; }
  .brand--small .brand__dot { width: 16px; height: 16px; margin-bottom: 2px; }
  .brand--large { left: 0; right: 0; top: 58px; font-size: 31px; }
  .brand--large .brand__dot { width: 40px; height: 40px; margin-bottom: 4px; }

  /* cover */
  .cover-band { left: 0; top: 73px; width: 544px; height: 211px; background: var(--band); }
  .cover-panel { top: 4px; height: 203px; }
  .cover-panel--left  { left: 4px;   width: 261px; background: var(--photo-grey); }
  .cover-panel--right { left: 272px; width: 261px; background: var(--photo-blue); }
  .cover-photo { top: 0; height: 203px; }
  .cover-panel--left .cover-photo  { left: 59px; width: 136px; top: 7px; height: 193px; background: linear-gradient(180deg, #f4f4f4 0%, #6b5a45 25%, #3c3024 100%); }
  .cover-panel--right .cover-photo { left: 66px; width: 132px; background: linear-gradient(180deg, #a9c7e6 0%, #6e8fb2 45%, #3e5570 100%); }
  .cover-title { left: 0; right: 0; top: 310px; text-align: center; font-size: 20px; font-weight: 700; }
  .cover-subtitle { left: 0; right: 0; top: 343px; text-align: center; font-size: 16px; }
  .cover-url { left: 0; right: 0; top: 382px; text-align: center; font-size: 11px; color: var(--brand); }

  /* slide headings */
  .slide-heading { top: 24px; width: 280px; text-align: center; font-size: 20px; font-weight: 700; color: var(--brand); }
  .slide-heading::after { content: ""; display: block; width: 190px; height: 2px; margin: 6px auto 0; background: var(--rule); }
  .slide--points .slide-heading { left: 140px; }
  .slide--chart .slide-heading  { left: 138px; }
  .slide--points .brand--small, .slide--chart .brand--small { left: 392px; top: 20px; }

  /* points */
  .point-photo { width: 94px; height: 66px; border-radius: 50%; background: linear-gradient(180deg, #9bb6c7 0%, #b5653f 55%, #7a4a32 100%); }
  .point-list { list-style: none; font-family: "Carlito", Calibri, sans-serif; font-size: 12px; line-height: 16px; }
  .point-list li::before { content: "✓"; margin-right: 2px; }

  /* page number */
  .page-marker { left: 8px; top: 351px; width: 28px; height: 28px; border-radius: 50%; background: var(--page-dot); color: #fff; font-size: 11px; text-align: center; line-height: 28px; }
  .page-rule { left: 36px; right: 0; top: 364px; height: 2px; background: var(--rule); }

  /* chart */
  .chart { left: 85px; top: 88px; }
  .chart text { font-family: "Arimo", Arial, sans-serif; fill: #222; }

  /* thank you */
  .thanks-photo { left: 70px; top: 201px; width: 396px; height: 102px; background: linear-gradient(180deg, #ffffff 0%, #ececec 45%, #d7d7d7 60%, #ffffff 100%); }
</style>
</head>
<body>

<section class="slide slide--cover" aria-label="Cover slide">
  <div class="brand brand--cover"><span class="brand__dot"></span>Fermoso Habitar</div>
  <div class="abs cover-band">
    <div class="abs cover-panel cover-panel--left">
      <div class="abs cover-photo" role="img" aria-label="Photo of a historic stone high-rise building"></div>
    </div>
    <div class="abs cover-panel cover-panel--right">
      <div class="abs cover-photo" role="img" aria-label="Photo of a modern glass office tower against blue sky"></div>
    </div>
  </div>
  <h1 class="abs cover-title">Your Presentation Title here</h1>
  <p class="abs cover-subtitle">Sub title here</p>
  <p class="abs cover-url">www.fermosohabitar.pt</p>
</section>

<section class="slide slide--points" aria-label="Points slide">
  <h2 class="abs slide-heading">Your sub title here</h2>
  <div class="brand brand--small"><span class="brand__dot"></span>Fermoso Habitar</div>

  <div class="abs point-photo" style="left:20px;top:101px" role="img" aria-label="Photo of a colourful street-side building"></div>
  <ul class="abs point-list" style="left:120px;top:109px"><li>Your Points come here</li><li>Your Points come here</li><li>Your Points come here</li></ul>

  <div class="abs point-photo" style="left:289px;top:101px" role="img" aria-label="Photo of a colourful street-side building"></div>
  <ul class="abs point-list" style="left:388px;top:109px"><li>Your Points come here</li><li>Your Points come here</li><li>Your Points come here</li></ul>

  <div class="abs point-photo" style="left:20px;top:211px" role="img" aria-label="Photo of a red brick corner building"></div>
  <ul class="abs point-list" style="left:120px;top:218px"><li>Your Points come here</li><li>Your Points come here</li><li>Your Points come here</li></ul>

  <div class="abs point-photo" style="left:289px;top:211px" role="img" aria-label="Photo of a red brick corner building"></div>
  <ul class="abs point-list" style="left:388px;top:218px"><li>Your Points come here</li><li>Your Points come here</li><li>Your Points come here</li></ul>

  <div class="abs page-rule"></div>
  <div class="abs page-marker">1</div>
</section>

<section class="slide slide--chart" aria-label="Chart slide">
  <h2 class="abs slide-heading">Your Chart comes here</h2>
  <div class="brand brand--small"><span class="brand__dot"></span>Fermoso Habitar</div>

  <svg class="abs chart" width="360" height="240" viewBox="0 0 360 240" aria-label="Bar chart of three series across four categories">
    <g stroke="var(--grid)" stroke-width="1">
      <line x1="30" y1="204" x2="250" y2="204"/>
      <line x1="30" y1="185" x2="250" y2="185"/>
      <line x1="30" y1="166" x2="250" y2="166"/>
      <line x1="30" y1="147" x2="250" y2="147"/>
      <line x1="30" y1="128" x2="250" y2="128"/>
      <line x1="30" y1="109" x2="250" y2="109"/>
      <line x1="30" y1="90"  x2="250" y2="90"/>
      <line x1="30" y1="71"  x2="250" y2="71"/>
      <line x1="30" y1="52"  x2="250" y2="52"/>
      <line x1="30" y1="33"  x2="250" y2="33"/>
      <line x1="30" y1="14"  x2="250" y2="14"/>
      <line x1="30" y1="14"  x2="30"  y2="204"/>
    </g>
    <g font-size="8" text-anchor="end">
      <text x="22" y="207">0</text><text x="22" y="188">0.5</text><text x="22" y="169">1</text>
      <text x="22" y="150">1.5</text><text x="22" y="131">2</text><text x="22" y="112">2.5</text>
      <text x="22" y="93">3</text><text x="22" y="74">3.5</text><text x="22" y="55">4</text>
      <text x="22" y="36">4.5</text><text x="22" y="17">5</text>
    </g>
    <g>
      <rect x="38"  y="41"  width="12" height="163" fill="var(--series-1)"/>
      <rect x="51"  y="113" width="12" height="91"  fill="var(--series-2)"/>
      <rect x="64"  y="128" width="12" height="76"  fill="var(--series-3)"/>

      <rect x="93"  y="109" width="12" height="95"  fill="var(--series-1)"/>
      <rect x="106" y="37"  width="12" height="167" fill="var(--series-2)"/>
      <rect x="119" y="128" width="12" height="76"  fill="var(--series-3)"/>

      <rect x="148" y="71"  width="12" height="133" fill="var(--series-1)"/>
      <rect x="161" y="136" width="12" height="68"  fill="var(--series-2)"/>
      <rect x="174" y="90"  width="12" height="114" fill="var(--series-3)"/>

      <rect x="203" y="33"  width="12" height="171" fill="var(--series-1)"/>
      <rect x="216" y="98"  width="12" height="106" fill="var(--series-2)"/>
      <rect x="229" y="14"  width="12" height="190" fill="var(--series-3)"/>
    </g>
    <g font-size="7" text-anchor="middle">
      <text x="57"  y="222">Category 1</text>
      <text x="112" y="222">Category 2</text>
      <text x="167" y="222">Category 3</text>
      <text x="222" y="222">Category 4</text>
    </g>
    <g font-size="7">
      <rect x="270" y="106" width="6" height="6" fill="var(--series-1)"/><text x="280" y="112">Series 1</text>
      <rect x="270" y="118" width="6" height="6" fill="var(--series-2)"/><text x="280" y="124">Series 2</text>
      <rect x="270" y="130" width="6" height="6" fill="var(--series-3)"/><text x="280" y="136">Series 3</text>
    </g>
  </svg>

  <div class="abs page-rule"></div>
  <div class="abs page-marker">2</div>
</section>

<section class="slide slide--thanks" aria-label="Closing slide">
  <div class="brand brand--large"><span class="brand__dot"></span>Fermoso Habitar</div>
  <div class="abs thanks-photo" role="img" aria-label="Photo of white letter dice spelling thank you with a soft reflection"></div>
  <div class="abs page-rule"></div>
  <div class="abs page-marker">3</div>
</section>

</body>
</html>
```